Advertisement Design Project

Attached is the information I need in a big color ad

10X11 that will go in a weekly local paper.
I am open to color and graphics-no pictures of people please.

My logo is also attached, which I would like in the ad.

Sorry for the short notice-I just got a deal on the space and it is due Friday.

```html
<!DOCTYPE html>
<html lang="en">
<head>
<meta charset="utf-8">
<title>Estate Planning Workshop</title>
<link rel="stylesheet" href="https://fonts.googleapis.com/css2?family=Alike&display=swap">
<style>
  :root {
    --gold: #f5b335;
    --gold-pale: #fde9bf;
    --grey: #7b7b7b;
    --ink: #333333;
    --paper: #ffffff;
  }
  * { margin: 0; padding: 0; box-sizing: border-box; }
  html, body { width: 1200px; height: 1091px; overflow: hidden; background: var(--paper); }
  body { font-family: "Alike", Georgia, serif; color: var(--ink); position: relative; }

  .frame { position: absolute; left: 0; top: 0; }

  .brand { position: absolute; left: 1005px; top: 48px; width: 170px; text-align: center; color: var(--gold); font-size: 27px; line-height: 1.15; }
  .brand-dot { display: block; width: 34px; height: 34px; border-radius: 50%; background: var(--gold); margin: 0 auto 14px; }

  .headline { position: absolute; left: 78px; top: 62px; font-size: 82px; font-weight: 400; color: var(--gold); line-height: 1; white-space: nowrap; }
  .headline-tag { position: absolute; left: 752px; top: 102px; font-size: 43px; color: var(--grey); letter-spacing: 1px; }
  .subhead { position: absolute; left: 78px; top: 174px; font-size: 56px; font-weight: 400; color: var(--grey); white-space: nowrap; }

  .questions { position: absolute; left: 80px; top: 288px; list-style: none; font-size: 29px; line-height: 38.5px; color: var(--ink); }
  .questions li { position: relative; padding-left: 20px; white-space: nowrap; }
  .questions li::before { content: ""; position: absolute; left: 0; top: 17px; width: 8px; height: 8px; border-radius: 50%; background: var(--gold); }

  .values { position: absolute; right: 64px; top: 290px; text-align: right; font-size: 67px; line-height: 92px; color: var(--gold-pale); }

  .schedule { position: absolute; right: 80px; top: 624px; text-align: right; font-size: 28px; line-height: 36px; }
  .label { color: var(--gold); }

  .presenter { position: absolute; left: 86px; top: 740px; font-size: 28px; line-height: 40px; }
  .venue { position: absolute; right: 80px; top: 774px; text-align: right; font-size: 28px; line-height: 40px; }

  .tagline { position: absolute; left: 0; width: 1200px; top: 925px; text-align: center; font-style: italic; font-size: 30px; color: var(--gold); }
  .reservation { position: absolute; left: 0; width: 1200px; top: 978px; text-align: center; font-size: 30px; color: var(--ink); }
</style>
</head>
<body>
  <svg class="frame" width="1200" height="1091" viewBox="0 0 1200 1091" aria-hidden="true">
    <path d="M990 37 H78 Q37 37 37 78 V1015 Q37 1056 78 1056 H1130 Q1168 1056 1168 1015 V268"
          fill="none" stroke="var(--gold)" stroke-width="4"/>
  </svg>

  <div class="brand"><span class="brand-dot"></span>Ellison Estate Law</div>

  <h1 class="headline">New Tax Laws</h1>
  <span class="headline-tag">TRUSTS</span>
  <h2 class="subhead">Annuities and Long Term Care</h2>

  <ul class="questions">
    <li>Come learn what you need to know</li>
    <li>Is a living trust right for me?</li>
    <li>Does my existing Trust need to be changed?</li>
    <li>Why does Joint Tenancy create tax problems?</li>
    <li>I have a will, isn’t that enough?</li>
    <li>Why do I need powers of attorney?</li>
    <li>How much are inheritance taxes?</li>
    <li>What are the new Affordable Care Act taxes?</li>
    <li>How does Long Term Care insurance work?</li>
    <li>The average cost of long term care is over 80K<br>&nbsp;a year - how do I plan for those costs?</li>
  </ul>

  <div class="values">Trust<br>Relationship<br>Integrity</div>

  <div class="schedule">
    <div class="label">Workshop Times:</div>
    <div>September 19th&nbsp; 2013</div>
    <div>1-2:30pm and 6-7:30pm</div>
  </div>

  <div class="presenter">
    <div class="label">Presented By:</div>
    <div>dana mae ellison</div>
    <div>Attorney at Law</div>
    <div>1420 Cedar Lane, Millbrook.</div>
  </div>

  <div class="venue">
    <div>Harborview Coast Inn</div>
    <div>2250 Shoreline Court,</div>
    <div>Bayside, California 95000</div>
  </div>

  <p class="tagline">Helping&nbsp; Families plan their estates for over 20 years.</p>
  <p class="reservation">Seating is limited for a Reservation please call:&nbsp; (555)&nbsp; 014-2200</p>
</body>
</html>
```